Business Cards and Stationery for Consulting Firm
Meridian Stone Partners
Business Cards and Stationery for Consulting Firm - Consulting
Creative Brief
Professional
Leo Farrow, PE, LEED AP
President
2786 Harlow St Kensington, MD 20817
leo.farrow@meridianstonepartners.example
www.meridianstonepartners.example
We want a black background with only the logo. We want the logo to have a metallic finish on the back side only.
mspadmin mspadmin
Please make sure to use image file "31 MSP Revision" on the back of the business card, because we want the back of the business card to have a black background. Use image file "21 MSP Revision" when working with a white background.

```html
<!DOCTYPE html>
<html lang="en">
<head>
<meta charset="utf-8">
<title>Meridian Stone Partners — Business Cards</title>
<link rel="stylesheet" href="https://fonts.googleapis.com/css2?family=Montserrat:wght@400;800&display=swap">
<style>
  :root {
    --stage: #d9d6d1;
    --ink: #0c0c0c;
    --paper: #ffffff;
    --grey: #8a8a8a;
    --silver: #d0d0d0;
    --light-text: #f2f2f2;
  }
  * { margin: 0; padding: 0; box-sizing: border-box; }
  html, body { width: 1200px; height: 904px; overflow: hidden; }
  body {
    background: var(--stage);
    font-family: "Montserrat", Arial, sans-serif;
    position: relative;
  }
  .card {
    position: absolute;
    width: 600px;
    height: 340px;
    box-shadow: 0 10px 28px rgba(0,0,0,0.28);
    overflow: hidden;
  }
  .card-back {
    left: 60px; top: 100px;
    background: var(--ink);
    color: var(--silver);
  }
  .card-front {
    left: 560px; top: 480px;
    background: var(--paper);
  }
  .brand {
    display: flex;
    align-items: center;
    gap: 10px;
    font-weight: 800;
    text-transform: uppercase;
    letter-spacing: 0.5px;
    white-space: nowrap;
  }
  .brand-square { width: 20px; height: 20px; flex: none; }
  .card-back .brand {
    position: absolute;
    left: 130px; top: 128px;
    font-size: 21px;
    color: var(--silver);
  }
  .card-back .brand-square { background: var(--silver); }
  .card-back .web {
    position: absolute;
    left: 130px; top: 190px;
    font-size: 15px;
    color: var(--light-text);
  }
  .swoosh { position: absolute; inset: 0; }
  .card-front .brand {
    position: absolute;
    left: 30px; top: 150px;
    font-size: 13px;
    gap: 8px;
    color: var(--ink);
  }
  .card-front .brand-square { width: 15px; height: 15px; background: var(--ink); }
  .contact {
    position: absolute;
    left: 345px; top: 128px;
    color: var(--light-text);
    font-size: 9.5px;
    line-height: 1.6;
  }
  .contact .name { font-size: 11.5px; }
  .contact .role { font-size: 9px; margin-bottom: 8px; }
  .contact .line { display: flex; align-items: center; gap: 5px; white-space: nowrap; }
  .contact svg { width: 10px; height: 10px; flex: none; }
</style>
</head>
<body>

<section class="card card-back" aria-label="Business card back">
  <div class="brand"><span class="brand-square"></span>Meridian Stone Partners</div>
  <p class="web">www.meridianstonepartners.example</p>
</section>

<section class="card card-front" aria-label="Business card front">
  <svg class="swoosh" viewBox="0 0 600 340" preserveAspectRatio="none" aria-hidden="true">
    <path d="M330 0 C270 60 340 140 270 220 C220 275 150 310 110 340 L600 340 L600 0 Z" fill="var(--grey)"/>
    <path d="M352 0 C292 60 362 140 292 220 C242 275 180 310 145 340 L600 340 L600 0 Z" fill="var(--ink)"/>
    <path d="M330 0 C270 60 340 140 270 220 C220 275 150 310 110 340" fill="none" stroke="var(--silver)" stroke-width="3"/>
  </svg>

  <div class="brand"><span class="brand-square"></span>Meridian Stone Partners</div>

  <div class="contact">
    <p class="name">Leo Farrow, PE, LEED AP</p>
    <p class="role">President</p>
    <p class="line">2786 Harlow St Kensington,</p>
    <p class="line">MD 20817</p>
    <p class="line">
      <svg viewBox="0 0 12 12"><rect x="3" y="0.5" width="6" height="11" rx="1.2" fill="none" stroke="currentColor"/><circle cx="6" cy="9.5" r="0.7" fill="currentColor"/></svg>
      954-555-0147
    </p>
    <p class="line">
      <svg viewBox="0 0 12 12"><rect x="0.5" y="2.5" width="11" height="7" fill="none" stroke="currentColor"/><path d="M0.5 2.5 L6 7 L11.5 2.5" fill="none" stroke="currentColor"/></svg>
      leo.farrow@meridianstonepartners.example
    </p>
    <p class="line">
      <svg viewBox="0 0 12 12"><circle cx="6" cy="6" r="5.2" fill="none" stroke="currentColor"/><ellipse cx="6" cy="6" rx="2.2" ry="5.2" fill="none" stroke="currentColor"/><path d="M1 6 H11" stroke="currentColor"/></svg>
      www.meridianstonepartners.example
    </p>
  </div>
</section>

</body>
</html>
```